Business Card Design Project

I want a cleaner business card and envelope then what we have now, its too crowded.
Updates

I update with logo, this can be changed anyway you feel it looks best. I also have put gaurantee on there and extended time, this is my first time doing this. Also gave an example of current card

Target Market(s)

a wide array of customers from lattice 700 to small companies and cleints

Industry/Entity Type

Business

Requirements
Must have
• Need to have address, telephone number email
Nice to have
• a sharp professional card that stands out but is still very clean.
Should not have
• Not crazy looking

```html
<!DOCTYPE html>
<html lang="en">
<head>
<meta charset="utf-8">
<title>Halverin Insurance Group – Envelope</title>
<link rel="stylesheet" href="https://fonts.googleapis.com/css2?family=Montserrat:wght@400&family=Source+Sans+3:wght@400&display=swap">
<style>
  :root {
    --backdrop: #1c1c1c;
    --paper: #e8e2d0;
    --ink: #1e1c1a;
    --ink-soft: #4a4844;
    --mark: #8e8c88;
  }
  * { margin: 0; padding: 0; box-sizing: border-box; }
  html, body {
    width: 1200px;
    height: 907px;
    overflow: hidden;
    background: var(--backdrop);
  }
  .canvas {
    position: relative;
    width: 1200px;
    height: 907px;
  }
  .envelope {
    position: absolute;
    left: 89px;
    top: 211px;
    width: 1042px;
    height: 521px;
    background: var(--paper);
  }
  .brand-square {
    position: absolute;
    left: 47px;
    top: 54px;
    width: 60px;
    height: 60px;
    background: var(--mark);
  }
  .brand-name {
    position: absolute;
    left: 127px;
    top: 62px;
    font-family: "Montserrat", sans-serif;
    font-weight: 400;
    color: var(--ink);
    line-height: 1;
    white-space: nowrap;
  }
  .brand-name .primary {
    display: block;
    font-size: 24px;
    letter-spacing: 5px;
  }
  .brand-name .secondary {
    display: block;
    margin-top: 5px;
    font-size: 13px;
    letter-spacing: 3.4px;
  }
  .return-address {
    position: absolute;
    left: 132px;
    top: 132px;
    font-family: "Source Sans 3", sans-serif;
    font-size: 14.5px;
    line-height: 19px;
    color: var(--ink-soft);
    font-style: normal;
    white-space: nowrap;
  }
</style>
</head>
<body>
  <main class="canvas">
    <section class="envelope">
      <span class="brand-square" aria-hidden="true"></span>
      <p class="brand-name">
        <span class="primary">HALVERIN</span>
        <span class="secondary">INSURANCE GROUP</span>
      </p>
      <address class="return-address">
        18230 Calder Ave.<br>
        Westbrook Hills, MI 48210
      </address>
    </section>
  </main>
</body>
</html>
```